Resume redesign

I'm a researcher who works with web design companies. I'm updating my resume but want more than the standard black and white wall of text. The content is updated, what I need is a design to make it readable, or in the words of my friend the hiring manager 'it needs to have high scan value'. It has to strike some balance between professionalism and readability.

There are two versions of my resume attached. I'm willing to cut some information if needed or reword things to simplify them. It would be great if it could be cut down to 2 pages, although this may require eliminating the publications section (which is fine).

```html
<!DOCTYPE html>
<html lang="en">
<head>
<meta charset="utf-8">
<title>Resume – Education &amp; Publications</title>
<link rel="stylesheet" href="https://fonts.googleapis.com/css2?family=Arimo:wght@400&family=Roboto+Slab:wght@300;400;700&display=swap">
<style>
  :root {
    --page: #ffffff;
    --band: #3d3d3d;
    --band-text: #a6a6a6;
    --label-light: #e8e8e8;
    --label-dark: #111111;
    --body-text: #8c8c8c;
  }
  * { margin: 0; padding: 0; box-sizing: border-box; }
  html, body {
    width: 836px;
    height: 1200px;
    overflow: hidden;
    background: var(--page);
  }
  body {
    position: relative;
    font-family: "Roboto Slab", Georgia, serif;
  }
  .education-band {
    position: absolute;
    left: 60px;
    top: 86px;
    width: 690px;
    height: 224px;
    background: var(--band);
  }
  .section-label {
    position: absolute;
    font-family: "Arimo", Arial, sans-serif;
    text-transform: uppercase;
  }
  .education-band .section-label {
    left: 61px;
    top: 103px;
    font-weight: 400;
    font-size: 13.5px;
    letter-spacing: 0.2px;
    color: var(--label-light);
  }
  .education-list {
    position: absolute;
    left: 353px;
    top: 13px;
    width: 328px;
    list-style: none;
    color: var(--band-text);
    font-weight: 300;
    font-size: 13.6px;
    line-height: 17.5px;
    letter-spacing: 0.3px;
  }
  .education-list li { margin-bottom: 17.5px; }
  .education-list .certification { font-style: italic; }
  .publications-label {
    left: 121px;
    top: 327px;
    font-family: "Roboto Slab", Georgia, serif;
    font-weight: 700;
    font-size: 14px;
    letter-spacing: 0.3px;
    color: var(--label-dark);
  }
  .publication-list {
    position: absolute;
    left: 413px;
    top: 324px;
    width: 326px;
    list-style: none;
    font-family: "Arimo", Arial, sans-serif;
    color: var(--body-text);
    font-size: 11.6px;
    line-height: 14.7px;
  }
  .publication-list li { margin-bottom: 14px; }
</style>
</head>
<body>
  <section class="education-band">
    <h2 class="section-label">Education &amp; Certifications</h2>
    <ul class="education-list">
      <li>Ph.D. in Anthropology, Research Methodology<br>Southern Coast University</li>
      <li>Master of Business Administration<br>Delta Plains University</li>
      <li>Bachelor of Arts in Anthropology<br>Prairie State University</li>
      <li class="certification">Civic Science Foundation Summer Institute for Research Design in Cultural Anthropology</li>
    </ul>
  </section>

  <h2 class="section-label publications-label">Publications</h2>
  <ul class="publication-list">
    <li>Hale, Daniel R. and Walter K. Brenn (2011) "Patterns in Research Credit: Training and Workplace Factors in Lab Culture" Journal of Lab Ethics 12: 104-131.</li>
    <li>Brenn, Walter K. and Daniel R. Hale (2011) "Patterns in Research Credit: A Review of How Teams Assign Credit" Journal of Lab Ethics 12: 58 - 79.</li>
    <li>Brenn, Walter K. and Daniel R. Hale (2011) "Patterns in Research Credit: Claiming, Missing and Declining Credit" Journal of Lab Ethics 12: 82-101. Hale, Nora B., Daniel R.</li>
    <li>Hale and Ivy Castell (2009) "Does word of mouth count? peer groups, trust, and new tool uptake" Rural Trade Letters 9: 2, pp 210-219.</li>
    <li>Porter, Glen and Daniel Hale (2008) "Seasonal Residence: a field study of coastal towns" Regional Census Bulletin 14: 301-318.</li>
    <li>Porter, Glen and Daniel Hale (2007) "Movers, Returners, and Stayers: Winter Travel Patterns of Retirees in Coastal Towns" Later Life Research Notes 33B:2, S114-121.</li>
    <li>Oliver T. Marsh, Simon Ashdown, E. Martin Coyle and Daniel Hale. (2007) "How Reliable Are Short Chains in Acquaintance Graphs" Ties &amp; Links Quarterly 19:3, pp 41-52.</li>
    <li>Ashdown, Simon, Daniel Hale, Paul Everly, and Owen Tallis. (2007) "Sorting the Role of Effort from Setting in Reply Rates for Phone Surveys" Fieldwork Methods Digest 7:4, pp 90-106.</li>
  </ul>
</body>
</html>
```